Double Sided Business Card Design for Pet Services

My mom and I want to start a business for pets. We want to offer dog walking, pet sitting as well as boarding and grooming at our home. For the front of the business card, we want a logo that will capture all of our services. We want the name to be Bigotes, Inc., which means little paws in Spanish. Perhaps, there could be little paws or just a little paw implemented within the word Bigotes. Or we would want a cat and a dog by the word Bigotes. We have a cat and a dog at home, and we would be really happy if they could be a part of the business card. It does not have to be anything crazy. Just an outline of a cat or a dog would be awesome. Please see uploaded file.
As for the back of the card, we would want little paws all over the card or we would want a collar, leash, grooming scissor, dog/cat bowl, bone, fish, or toy to show all of the services that we provide. Along with either the many paws or many pet objects, we would want to add our information, such as name (Lorenza Mireles), telephone numbers (555) 812-3762, e-mail addresses bigotesinc@correomail.net, etc.
We would also want a catch phrase to go on the back of the card, such as "WE STRIVE FOR HAPPY TAILS!" Or "We strive for happy tails." or "A paw-bulous service is guaranteed!"
As for colors, we would not want that many. We would want perhaps white and blue. We would want soft colors that will stand out and make an impression. The same goes with the text. An elegant text would be nice. Or perhaps a text with bold letters. We are excited to see the results, but we are also excited to see your creative ideas and what you will bring to the table.

Target Market(s)

Pet Owners

Contact Information for Business Card

For the front of the business card, we want a logo that will capture all of our services. We want the name to be Bigotes, Inc., which means little paws in Spanish. Perhaps, there could be little paws or just a little paw implemented within the word Bigotes. Or we would want a cat and a dog by the word Bigotes. We have a cat and a dog at home, and we would be really happy if they could be a part of the business card. It does not have to be anything crazy. Just an outline of a cat or a dog would be awesome. Please see uploaded file.
As for the back of the card, we would want little paws all over the card or we would want a collar, leash, grooming scissor, dog/cat bowl, bone, fish, or toy to show all of the services that we provide. Along with either the many paws or many pet objects, we would want to add our information, such as name, telephone numbers, e-mail addresses, etc. We would also want a catch phrase to go on the back of the card, such as "WE STRIVE FOR HAPPY TAILS!" Or "We strive happy tails." or "A paw-bulous service is guaranteed!" Or if there is a way to put the catch phrase in the front of the card. We are open to seeing variety.

Logo Text

Bigotes, Inc

Font styles to use
Serif
Script

Colors
ffffff
33a6d7
145ea8

Requirements
Must have
• My project must be a double sided business card.

```html
<!DOCTYPE html>
<html lang="en">
<head>
<meta charset="utf-8">
<title>Bigotes, Inc. – Business Card</title>
<link rel="stylesheet" href="https://fonts.googleapis.com/css2?family=Cinzel:wght@400;600&family=Hind:wght@600&family=Arimo:wght@400;700&display=swap">
<style>
  :root {
    --stage: #e6e8eb;
    --paper: #f4f4f4;
    --navy: #1a5ca8;
    --blue: #1460aa;
    --sky: #33a6d7;
    --ink: #1b1b1b;
    --rule: #7a7a7a;
    --white: #ffffff;
  }
  * { margin: 0; padding: 0; box-sizing: border-box; }
  html, body { width: 1200px; height: 1200px; overflow: hidden; }
  body { background: var(--stage); position: relative; font-family: "Arimo", Arial, sans-serif; }

  .card {
    position: absolute; top: 310px; width: 364px; height: 594px;
    box-shadow: 2px 3px 6px rgba(0,0,0,0.25); overflow: hidden;
  }
  .card--front { left: 234px; background: var(--paper); text-align: center; }
  .card--back { left: 630px; width: 366px; background: var(--blue); }

  .brand-dot {
    position: absolute; left: 132px; top: 70px; width: 100px; height: 100px;
    border-radius: 50%; background: var(--navy);
  }
  .brand-name {
    position: absolute; top: 230px; left: 0; width: 100%;
    font-family: "Cinzel", serif; font-weight: 600; font-size: 43px;
    color: var(--navy); letter-spacing: -0.5px; line-height: 1;
  }
  .brand-tag {
    position: absolute; top: 277px; left: 0; width: 100%;
    font-family: "Hind", sans-serif; font-weight: 600; font-size: 25px;
    letter-spacing: 2px; color: var(--sky); line-height: 1;
  }
  .person {
    position: absolute; top: 338px; left: 0; width: 100%;
    font-family: "Cinzel", serif; font-weight: 400; font-size: 24px;
    color: var(--navy); line-height: 1;
  }
  .person .surname { color: var(--sky); }
  .role { position: absolute; top: 362px; left: 0; width: 100%; font-size: 17px; color: var(--ink); }
  .rule { position: absolute; left: 78px; width: 208px; height: 1px; background: var(--rule); }
  .rule--top { top: 390px; }
  .rule--bottom { top: 498px; }
  .contact {
    position: absolute; top: 400px; left: 0; width: 100%;
    font-size: 16.5px; line-height: 21.5px; color: var(--ink); list-style: none;
  }
  .contact b { color: var(--navy); }
  .contact .web { font-weight: 700; color: var(--navy); }
  .contact .web span { color: var(--sky); }
  .address {
    position: absolute; top: 508px; left: 0; width: 100%;
    font-size: 16.5px; line-height: 21px; color: var(--ink); font-style: normal;
  }

  .back-art { position: absolute; inset: 0; }
  .tagline {
    position: absolute; top: 529px; left: 0; width: 100%; text-align: center;
    font-weight: 700; font-size: 17px; letter-spacing: 0.3px; color: var(--navy);
  }
</style>
</head>
<body>
  <section class="card card--front" aria-label="Card front">
    <div class="brand-dot"></div>
    <h1 class="brand-name">BIGOTES, INC.</h1>
    <p class="brand-tag">PET SERVICES</p>
    <h2 class="person">LORENZA <span class="surname">MIRELES</span></h2>
    <p class="role">Managing Director</p>
    <div class="rule rule--top"></div>
    <ul class="contact">
      <li><b>P:</b> (555) 812-3762</li>
      <li><b>M:</b> (555) 812-3762</li>
      <li><b>E:</b> bigotesinc@correomail.net</li>
      <li class="web">www.<span>bigotesinc</span>.net</li>
    </ul>
    <div class="rule rule--bottom"></div>
    <address class="address">12345, Address Goes Here<br>Country Name, 123456.</address>
  </section>

  <section class="card card--back" aria-label="Card back">
    <svg class="back-art" width="366" height="594" viewBox="0 0 366 594">
      <path d="M0 480 C60 400 110 335 183 335 C256 335 306 400 366 480 L366 594 L0 594 Z" fill="var(--sky)"/>
      <circle cx="183" cy="300" r="110" fill="var(--white)"/>
    </svg>
    <p class="tagline">WE STRIVE FOR HAPPY TAILS!</p>
  </section>
</body>
</html>
```